Artistically challenged consultant needs a sexy business card.

I need a business card design for my consultancy business. I work primarily in the pacific on international development program focusing on tourism, economic empowerment and training. I would like to use a light blue/green to reference the pacific and also a simple design of a sprouting coconut (photo attached for reference) to reference growth and development.
The business card should have icons for email, phone, skype, ABN and linked in.

Industry/Entity Type

Business

```html
<!DOCTYPE html>
<html lang="en">
<head>
<meta charset="utf-8">
<title>Mara Kellaway Consulting – Business Card</title>
<link href="https://fonts.googleapis.com/css2?family=PT+Sans:wght@400;700&display=swap" rel="stylesheet">
<style>
  :root {
    --stage: #5f5f5f;
    --card-blue: #8fd6f0;
    --card-glow: #ffffff;
    --title-ink: #4b5a66;
    --contact-ink: #3a3f44;
    --icon-grey: #6d7378;
    --sprout-green: #7fae3a;
    --nut-tan: #b89473;
  }
  * { box-sizing: border-box; margin: 0; padding: 0; }
  html, body {
    width: 1200px;
    height: 693px;
    overflow: hidden;
    background: var(--stage);
    font-family: "PT Sans", sans-serif;
  }
  .canvas { position: relative; width: 1200px; height: 693px; }
  .card {
    position: absolute;
    top: 167px;
    width: 508px;
    height: 289px;
    border-radius: 17px;
    overflow: hidden;
  }
  .card--front {
    left: 68px;
    background: radial-gradient(ellipse 300px 230px at 30% 56%, var(--card-glow) 0%, #dff3fb 35%, var(--card-blue) 100%);
  }
  .card--back {
    left: 624px;
    background: var(--card-blue);
  }
  .sprout-mark {
    position: absolute;
    left: 110px;
    top: 54px;
    width: 86px;
    height: 150px;
    border-radius: 40% 40% 45% 45%;
    background: linear-gradient(180deg, rgba(127,174,58,0.55) 0%, rgba(127,174,58,0.25) 45%, var(--nut-tan) 72%, #a07f60 100%);
  }
  .company-name {
    position: absolute;
    left: 246px;
    top: 87px;
    font-size: 19px;
    font-weight: 400;
    color: var(--title-ink);
    letter-spacing: 0.2px;
  }
  .contact-list {
    position: absolute;
    right: 34px;
    top: 176px;
    list-style: none;
  }
  .contact-item {
    display: flex;
    justify-content: flex-end;
    align-items: center;
    height: 18px;
    font-size: 11px;
    color: var(--contact-ink);
  }
  .contact-icon {
    width: 10px;
    height: 10px;
    margin-left: 7px;
    flex: none;
  }
</style>
</head>
<body>
<main class="canvas">
  <section class="card card--front" aria-label="Business card front">
    <div class="sprout-mark" role="img" aria-label="Illustration of a sprouting coconut with green leaves"></div>
    <h1 class="company-name">Mara Kellaway Consulting</h1>
    <ul class="contact-list">
      <li class="contact-item">+61 400 555 182
        <svg class="contact-icon" viewBox="0 0 10 10" aria-hidden="true">
          <rect width="10" height="10" rx="1" fill="var(--icon-grey)"/>
          <path d="M3 2.2 L4.2 3.6 L3.6 4.4 Q4.6 6 5.8 6.4 L6.5 5.8 L7.8 7 L7 8 Q3.8 7.6 2.2 3 Z" fill="#fff"/>
        </svg>
      </li>
      <li class="contact-item">mara kellaway
        <svg class="contact-icon" viewBox="0 0 10 10" aria-hidden="true"><rect width="10" height="10" rx="1" fill="var(--icon-grey)"/></svg>
      </li>
      <li class="contact-item">mara kellaway
        <svg class="contact-icon" viewBox="0 0 10 10" aria-hidden="true"><rect width="10" height="10" rx="1" fill="var(--icon-grey)"/></svg>
      </li>
      <li class="contact-item">www.kellawayadvisory.com
        <svg class="contact-icon" viewBox="0 0 10 10" aria-hidden="true">
          <rect width="10" height="10" rx="1" fill="var(--icon-grey)"/>
          <circle cx="5" cy="5" r="2.8" fill="none" stroke="#fff" stroke-width="0.8"/>
          <line x1="2.2" y1="5" x2="7.8" y2="5" stroke="#fff" stroke-width="0.8"/>
        </svg>
      </li>
      <li class="contact-item">mk@marakellawayconsulting.com
        <svg class="contact-icon" viewBox="0 0 10 10" aria-hidden="true">
          <rect width="10" height="10" rx="1" fill="var(--icon-grey)"/>
          <rect x="2" y="3" width="6" height="4" fill="none" stroke="#fff" stroke-width="0.8"/>
          <path d="M2 3 L5 5.4 L8 3" fill="none" stroke="#fff" stroke-width="0.8"/>
        </svg>
      </li>
    </ul>
  </section>
  <section class="card card--back" aria-label="Business card back"></section>
</main>
</body>
</html>
```